CGN Website (Cobalt Guard Networks)

We need a web design for an established company in Dubai, U.A.E, called Cobalt Guard Network. We provide a completed solutions in ICT-Information and Communication Technology (Computer, Networking, IP Telephony, Software and Hardware) and Security Systems (CCTV, Access Control, and System Integrator), our Services include Consultancy Planning and Design, Value Added Distribution, Implementation and Execution, Operations and Maintenance, Training and Development. We help our Clients to Develop and Secure their infrastructure. We would like to see design that use our logo theme, reflect our solutions and services, communicate to enterprise Technology and Security. Website must be responsive, Dynamic, symmetry or asymmetry or both.
Regards,

Target Market(s)

UAE

Industry/Entity Type

It Company

Coding

Coded - Design and coding required

Number of Pages Required

5+ page

Font styles to use
Sans Serif

Requirements
Must have
• Logo Theme, social media logos and links,
Nice to have
• Big blogs and banners
Should not have
• Many colors or congested design

```html
<!DOCTYPE html>
<html lang="en">
<head>
<meta charset="utf-8">
<title>Cobalt Guard Networks</title>
<link href="https://fonts.googleapis.com/css2?family=Open+Sans:wght@400;600;700&family=Oswald:wght@400;500&display=swap" rel="stylesheet">
<style>
:root{
  --yellow:#f2b705;
  --yellow-dark:#d89e00;
  --ink:#333;
  --text:#666;
  --header:#2b2b2b;
  --band:#4a4a4a;
  --light:#efefef;
  --line:#ddd;
  --white:#fff;
}
*{box-sizing:border-box;margin:0;padding:0}
html,body{width:1200px;height:2760px;overflow:hidden}
body{font-family:"Open Sans",Arial,sans-serif;color:var(--text);background:var(--white);font-size:14px}
.wrap{width:1040px;margin:0 auto;position:relative}
h2.section-title{font-family:"Oswald",Arial,sans-serif;font-weight:500;font-size:30px;color:var(--ink);text-align:center}
h2.section-title span{color:var(--yellow)}
/* header */
.site-header{height:140px;background:var(--header);position:relative}
.brand{position:absolute;left:80px;top:14px;display:flex;align-items:center;gap:12px}
.brand-name{font-family:"Oswald",sans-serif;color:var(--yellow);font-size:30px;line-height:1}
.brand-sub{display:block;font-size:15px;color:var(--yellow);letter-spacing:1px;margin-top:4px}
.social{position:absolute;right:80px;top:18px;display:flex;align-items:center;gap:8px;color:#ccc;font-size:13px}
.social i{width:22px;height:22px;border-radius:50%;background:#666;display:inline-block}
.phone{position:absolute;right:80px;top:52px;color:var(--yellow);font-size:18px;display:flex;align-items:center;gap:8px}
.main-nav{position:absolute;right:80px;bottom:0;display:flex}
.main-nav a{display:block;padding:12px 22px;color:#eee;text-decoration:none;font-size:15px;font-weight:600}
.main-nav a.active{background:var(--yellow);color:var(--header);border-radius:4px 4px 0 0}
/* banner */
.hero{height:420px;position:relative;background:linear-gradient(135deg,#0e2436,#1f4d6d 45%,#163048 70%,#0b1a28)}
.hero-art{position:absolute;inset:0}
.hero-caption{position:absolute;left:0;right:0;bottom:0;height:96px;background:rgba(20,20,20,.55);display:flex;align-items:center;justify-content:center}
.hero-caption p{font-family:"Oswald",sans-serif;color:var(--yellow);font-size:29px;text-align:center;line-height:1.25}
.hero-arrow{position:absolute;top:316px;width:30px;height:30px;background:rgba(0,0,0,.5);color:#fff;display:flex;align-items:center;justify-content:center;font-size:18px}
/* features */
.features{height:300px;padding-top:40px}
.feature-row{display:flex;justify-content:space-between}
.feature{width:240px;text-align:center}
.feature-icon{width:88px;height:88px;margin:0 auto 16px}
.feature h3{font-size:17px;color:var(--ink);font-weight:700;margin-bottom:8px}
.feature p{font-size:12.5px;line-height:1.5}
/* about */
.about{height:320px;background:var(--light);padding-top:30px}
.about .wrap{display:flex;justify-content:space-between}
.about-text{width:640px}
.about h2{font-family:"Oswald",sans-serif;font-weight:500;font-size:28px;color:var(--ink);margin-bottom:12px}
.about h2 span{color:var(--yellow)}
.about p{font-size:12.5px;line-height:1.6;margin-bottom:10px}
.read-more{color:var(--ink);font-weight:700;font-size:13px}
.videos{width:340px}
.video-frame{width:340px;height:200px;background:linear-gradient(135deg,#1c3b57,#0d1c2b);position:relative}
/* services */
.services{height:310px;background:var(--band);padding-top:26px}
.services h2.section-title{color:var(--white)}
.service-row{display:flex;justify-content:space-between;margin-top:26px;padding:0 40px}
.service{width:150px;text-align:center;color:var(--white);font-size:15px;line-height:1.35}
.service-icon{width:116px;height:116px;border-radius:50%;background:#bdbdbd;margin:0 auto 12px;display:flex;align-items:center;justify-content:center}
.service.active .service-icon{background:#6a6a6a;border:5px solid var(--yellow)}
.service.active{color:var(--yellow)}
/* partners */
.partners{height:230px;padding-top:44px}
.partner-row{display:flex;align-items:center;justify-content:space-between;margin-top:34px}
.partner{font-weight:700;font-size:19px;color:#555;display:flex;align-items:center;gap:6px}
.partner i{width:12px;height:12px;background:var(--yellow);display:inline-block}
.arrow-dark{font-size:30px;color:var(--ink)}
/* projects */
.projects{height:540px;background:#f7f7f7;padding-top:30px}
.project-grid{display:grid;grid-template-columns:repeat(3,300px);justify-content:space-between;row-gap:40px;margin-top:28px}
.project{height:180px;position:relative;border:4px solid #fff;box-shadow:0 1px 4px rgba(0,0,0,.2)}
.project-label{position:absolute;inset:0;background:rgba(60,60,60,.75);display:flex;align-items:center;justify-content:center;color:#fff;font-size:20px}
/* clients */
.clients{height:200px;background:#8f8f8f;padding-top:28px}
.clients h2.section-title{color:var(--white)}
.client-row{display:flex;align-items:center;justify-content:space-between;margin-top:24px}
.client{width:160px;height:64px;background:var(--white);display:flex;align-items:center;justify-content:center;gap:6px;font-weight:700;color:#2f5e86;font-size:16px}
.client i{width:10px;height:10px;border-radius:50%;background:#2f5e86}
.arrow-yellow{width:34px;height:34px;background:var(--yellow);color:var(--white);display:flex;align-items:center;justify-content:center;font-size:18px}
/* footer */
.site-footer{height:260px;background:var(--header);padding-top:34px;color:#ccc;font-size:13px}
.footer-cols{display:flex;gap:60px}
.site-footer h4{color:var(--white);font-size:15px;margin-bottom:14px}
.quick-links li{list-style:none;line-height:2}
.contact-line{display:flex;align-items:center;gap:8px;line-height:1.5;margin-bottom:8px}
.newsletter input{display:block;width:220px;height:28px;border:0;margin-bottom:8px;padding:0 8px;font-size:12px}
.btn{background:var(--yellow);color:var(--header);border:0;padding:6px 14px;font-weight:700;font-size:12px}
.footer-brand{position:absolute;right:0;top:0;width:230px;height:160px;background:#3b3b3b;display:flex;flex-direction:column;align-items:center;justify-content:center;gap:8px;text-align:center}
.copyright{height:40px;background:#1c1c1c;color:#999;font-size:12px;line-height:40px;padding-left:80px}
</style>
</head>
<body>

<header class="site-header">
  <div class="brand">
    <svg width="70" height="70" viewBox="0 0 70 70"><circle cx="35" cy="35" r="30" fill="none" stroke="#f2b705" stroke-width="6"/></svg>
    <div class="brand-name">Cobalt Guard<span class="brand-sub">NETWORKS</span></div>
  </div>
  <div class="social">Follow us on <i></i><i></i><i></i><i></i></div>
  <div class="phone">
    <svg width="18" height="18" viewBox="0 0 24 24"><path d="M6 2l4 4-2 3c1 3 4 6 7 7l3-2 4 4-3 4C10 22 2 14 2 5z" fill="#f2b705"/></svg>
    123 456 7890
  </div>
  <nav class="main-nav">
    <a class="active" href="#">Home</a><a href="#">About Us</a><a href="#">Services</a><a href="#">Testimonials</a><a href="#">Contact Us</a>
  </nav>
</header>

<section class="hero">
  <div class="hero-art" role="img" aria-label="Banner image: digital shield over a blue circuit board"></div>
  <div class="hero-arrow" style="right:124px">&#8249;</div>
  <div class="hero-arrow" style="right:90px">&#8250;</div>
  <div class="hero-caption"><p>We Provide A Complete Solution In ICT-Information,<br>Communication Technology And Security Systems</p></div>
</section>

<section class="features">
  <div class="wrap feature-row">
    <div class="feature">
      <svg class="feature-icon" viewBox="0 0 88 88"><circle cx="44" cy="44" r="40" fill="#fff" stroke="#f2b705" stroke-width="6"/><rect x="28" y="30" width="32" height="26" rx="3" fill="#f2b705"/><rect x="32" y="58" width="24" height="4" fill="#f2b705"/></svg>
      <h3>IP Telephony System</h3>
      <p>Reliable voice networks built for growing teams, linking every office and desk.</p>
    </div>
    <div class="feature">
      <svg class="feature-icon" viewBox="0 0 88 88"><circle cx="44" cy="44" r="40" fill="#fff" stroke="#f2b705" stroke-width="6"/><rect x="24" y="36" width="34" height="16" rx="3" fill="#f2b705"/><path d="M58 40l10-5v18l-10-5z" fill="#f2b705"/></svg>
      <h3>Security Systems</h3>
      <p>CCTV and access control that keep your sites watched and protected all day.</p>
    </div>
    <div class="feature">
      <svg class="feature-icon" viewBox="0 0 88 88"><circle cx="44" cy="44" r="40" fill="#fff" stroke="#f2b705" stroke-width="6"/><path d="M44 24c-8 0-13 6-13 13 0 10 13 25 13 25s13-15 13-25c0-7-5-13-13-13z" fill="#f2b705"/><circle cx="44" cy="37" r="5" fill="#fff"/></svg>
      <h3>Tracking and GPS</h3>
      <p>Live location tracking for fleets and assets across the whole region.</p>
    </div>
    <div class="feature">
      <svg class="feature-icon" viewBox="0 0 88 88"><circle cx="44" cy="44" r="40" fill="#fff" stroke="#f2b705" stroke-width="6"/><circle cx="44" cy="44" r="18" fill="none" stroke="#f2b705" stroke-width="4"/><path d="M26 44h36M44 26c-8 10-8 26 0 36M44 26c8 10 8 26 0 36" fill="none" stroke="#f2b705" stroke-width="3"/></svg>
      <h3>Online Services</h3>
      <p>Hosted tools and remote support that keep your business running online.</p>
    </div>
  </div>
</section>

<section class="about">
  <div class="wrap">
    <div class="about-text">
      <h2>About <span>Cobalt Guard Networks</span></h2>
      <p>Cobalt Guard Networks is an established technology company in Dubai, delivering complete solutions in information and communication technology. We design, supply and install computer networks, IP telephony, software and hardware for enterprises of every size. Our engineers work closely with each client from the first plan to the final handover, so every system fits the way the business really works.</p>
      <p>Our security division covers CCTV, access control and system integration, helping clients develop and secure their infrastructure. With trusted partners and a skilled team, we offer support, maintenance and training long after a project goes live.</p>
      <a class="read-more">Read More &rsaquo;</a>
    </div>
    <div class="videos">
      <h2>Latest <span>Videos</span></h2>
      <div class="video-frame" role="img" aria-label="Video thumbnail of a security control room">
        <svg width="340" height="200" viewBox="0 0 340 200" style="position:absolute;inset:0"><rect x="145" y="78" width="50" height="36" rx="8" fill="#cc2222"/><path d="M163 86l16 10-16 10z" fill="#fff"/><rect x="0" y="180" width="340" height="20" fill="rgba(0,0,0,.6)"/></svg>
      </div>
    </div>
  </div>
</section>

<section class="services">
  <h2 class="section-title">Our <span>Services</span></h2>
  <div class="wrap service-row">
    <div class="service active"><div class="service-icon"><svg width="56" height="56" viewBox="0 0 56 56"><circle cx="28" cy="28" r="20" fill="none" stroke="#fff" stroke-width="4"/><circle cx="28" cy="28" r="6" fill="#fff"/><path d="M28 2v12M28 42v12M2 28h12M42 28h12" stroke="#fff" stroke-width="4"/></svg></div>Consultancy<br>Planning and Design</div>
    <div class="service"><div class="service-icon"><svg width="56" height="56" viewBox="0 0 56 56"><rect x="22" y="6" width="12" height="12" fill="#fff"/><rect x="6" y="38" width="12" height="12" fill="#fff"/><rect x="22" y="38" width="12" height="12" fill="#fff"/><rect x="38" y="38" width="12" height="12" fill="#fff"/><path d="M28 18v20M12 38v-8h32v8" fill="none" stroke="#fff" stroke-width="3"/></svg></div>Value<br>Added Distribution</div>
    <div class="service"><div class="service-icon"><svg width="56" height="56" viewBox="0 0 56 56"><circle cx="20" cy="22" r="12" fill="none" stroke="#fff" stroke-width="6" stroke-dasharray="5 3"/><circle cx="38" cy="38" r="9" fill="none" stroke="#fff" stroke-width="5" stroke-dasharray="4 3"/></svg></div>Implementation<br>and Execution</div>
    <div class="service"><div class="service-icon"><svg width="56" height="56" viewBox="0 0 56 56"><path d="M10 46L34 22M46 46L22 22" stroke="#fff" stroke-width="6"/><circle cx="38" cy="16" r="8" fill="none" stroke="#fff" stroke-width="4"/><circle cx="18" cy="16" r="6" fill="#fff"/></svg></div>Operations<br>and Maintenance</div>
    <div class="service"><div class="service-icon"><svg width="56" height="56" viewBox="0 0 56 56"><circle cx="18" cy="18" r="7" fill="#fff"/><path d="M6 46c0-10 5-16 12-16s12 6 12 16z" fill="#fff"/><rect x="30" y="10" width="22" height="16" fill="none" stroke="#fff" stroke-width="3"/></svg></div>Training<br>and Development</div>
  </div>
</section>

<section class="partners">
  <h2 class="section-title">Key <span>Partners</span></h2>
  <div class="wrap partner-row">
    <span class="arrow-dark">&#8249;</span>
    <span class="partner"><i></i>Vantor</span>
    <span class="partner">Kelmaro</span>
    <span class="partner">Unisync</span>
    <span class="partner"><i></i>Brightsoft</span>
    <span class="partner">Corvane</span>
    <span class="partner"><i></i>Halvex</span>
    <span class="arrow-dark">&#8250;</span>
  </div>
</section>

<section class="projects">
  <h2 class="section-title">Major <span>Projects</span></h2>
  <div class="wrap project-grid">
    <div class="project" role="img" aria-label="Project photo: server room" style="background:linear-gradient(135deg,#9a9a9a,#6d6d6d)"><div class="project-label">Lorem ipsum dolor</div></div>
    <div class="project" role="img" aria-label="Project photo: data center racks" style="background:linear-gradient(135deg,#a58e6a,#5a4a38)"></div>
    <div class="project" role="img" aria-label="Project photo: equipment container" style="background:linear-gradient(135deg,#c9b489,#8d7a56)"></div>
    <div class="project" role="img" aria-label="Project photo: network cabinets" style="background:linear-gradient(135deg,#d4d4d4,#8e8e8e)"></div>
    <div class="project" role="img" aria-label="Project photo: cabling installation" style="background:linear-gradient(135deg,#c2b7a2,#7e705c)"></div>
    <div class="project" role="img" aria-label="Project photo: site containers" style="background:linear-gradient(135deg,#d7c49c,#9e8a62)"></div>
  </div>
</section>

<section class="clients">
  <h2 class="section-title">Major <span>Clients</span></h2>
  <div class="wrap client-row">
    <span class="arrow-yellow">&#8249;</span>
    <span class="client"><i></i>Meridian Sea</span>
    <span class="client">Ideora</span>
    <span class="client">Optivon</span>
    <span class="client"><i></i>Q-Drive</span>
    <span class="client">Sorelle</span>
    <span class="arrow-yellow">&#8250;</span>
  </div>
</section>

<footer class="site-footer">
  <div class="wrap">
    <div class="footer-cols">
      <div>
        <h4>Quick Link</h4>
        <ul class="quick-links"><li>Home</li><li>About Us</li><li>Services</li><li>Testimonials</li><li>Contact Us</li></ul>
      </div>
      <div>
        <h4>Contact Address</h4>
        <div class="contact-line"><svg width="16" height="16" viewBox="0 0 24 24"><path d="M12 2a7 7 0 0 0-7 7c0 5 7 13 7 13s7-8 7-13a7 7 0 0 0-7-7z" fill="#f2b705"/></svg><span>Cobalt Guard Networks<br>Business Bay, Dubai, U.A.E</span></div>
        <div class="contact-line"><svg width="16" height="16" viewBox="0 0 24 24"><path d="M6 2l4 4-2 3c1 3 4 6 7 7l3-2 4 4-3 4C10 22 2 14 2 5z" fill="#f2b705"/></svg>123 456 7890</div>
        <div class="contact-line"><svg width="16" height="16" viewBox="0 0 24 24"><path d="M6 2l4 4-2 3c1 3 4 6 7 7l3-2 4 4-3 4C10 22 2 14 2 5z" fill="#f2b705"/></svg>123 456 7890</div>
        <div class="contact-line"><svg width="16" height="16" viewBox="0 0 24 24"><rect x="2" y="5" width="20" height="14" fill="#f2b705"/><path d="M2 5l10 8 10-8" fill="none" stroke="#2b2b2b" stroke-width="2"/></svg>info@cobaltguardnetworks.com</div>
      </div>
      <div class="newsletter">
        <h4>Newsletter Signup</h4>
        <p style="margin-bottom:10px">Get our latest news and offers.</p>
        <input type="text" placeholder="Name">
        <input type="text" placeholder="Email address">
        <button class="btn">Subscribe</button>
      </div>
    </div>
    <div class="footer-brand">
      <svg width="60" height="60" viewBox="0 0 60 60"><circle cx="30" cy="30" r="25" fill="none" stroke="#f2b705" stroke-width="5"/></svg>
      <div class="brand-name" style="font-size:24px">Cobalt Guard<span class="brand-sub" style="font-size:13px">NETWORKS</span></div>
    </div>
  </div>
</footer>
<div class="copyright">Copyright 2015 by Cobalt Guard Networks. All Rights Reserved.</div>

</body>
</html>
```